HUSH: Hush Until Stories Happen school library event

I need two poster designs for Hush Until Stories Happen (HUSH) in BC, requested by the PCSMG--Pacific Coast School Media Guild. One should be for elementary students and one for high school. I want the date (Monday, October 26, 2020) and Hush Until Stories Happen. I would like the posters in English and in French. French is : Ferme Ton Écran Maintenant! I'm including last year's posters as examples. I would like to be able to print the poster files on 11x17 paper.

• -The phrase "Hush Until Stories Happen" for the English version; "Ferme Ton Écran Maintenant" for the French version.
-Include the organization name: Pacific Coast School Media Guild
-The date: Monday, October 26, 2020
• I would like the elementary version to be bright and colourful--fun for younger kids. I would like the high school version to be a bit more mature for the older students. Can still be bright and colourful.

```html
<!DOCTYPE html>
<html lang="en">
<head>
<meta charset="utf-8">
<title>Hush Until Stories Happen — Poster</title>
<link rel="stylesheet" href="https://fonts.googleapis.com/css2?family=Archivo+Black&family=Work+Sans:wght@600;700&display=swap">
<style>
  :root {
    --magenta: #c8155e;
    --wine: #6e0f2c;
    --deep: #3a0716;
    --yellow: #e2c21e;
    --white: #ffffff;
  }
  html, body {
    margin: 0;
    padding: 0;
    width: 800px;
    height: 1200px;
    overflow: hidden;
    background: var(--deep);
  }
  .poster {
    position: relative;
    width: 800px;
    height: 1200px;
    overflow: hidden;
  }
  .book-stack-photo {
    position: absolute;
    inset: 0;
    background:
      radial-gradient(ellipse 70% 60% at 35% 60%, rgba(214, 28, 104, 0.9), rgba(214, 28, 104, 0) 70%),
      linear-gradient(180deg, var(--wine) 0%, var(--magenta) 45%, var(--magenta) 70%, var(--wine) 100%);
  }
  .headline {
    position: absolute;
    inset: 0;
    width: 800px;
    height: 1200px;
  }
  .headline text {
    font-family: "Archivo Black", "Work Sans", sans-serif;
    font-size: 164px;
    fill: var(--yellow);
    letter-spacing: -2px;
  }
  .credit {
    position: absolute;
    left: 0;
    width: 800px;
    top: 986px;
    text-align: center;
    color: var(--white);
    font-family: "Work Sans", sans-serif;
  }
  .credit-lead {
    margin: 0 0 20px;
    font-size: 15px;
    font-weight: 600;
    letter-spacing: 4.5px;
  }
  .credit-org {
    margin: 0;
    font-size: 20px;
    font-weight: 700;
    line-height: 27px;
    letter-spacing: 0.5px;
  }
  .event-date {
    position: absolute;
    left: 0;
    width: 800px;
    top: 1118px;
    margin: 0;
    text-align: center;
    color: var(--yellow);
    font-family: "Work Sans", sans-serif;
    font-weight: 700;
    font-size: 44px;
    letter-spacing: -1.5px;
  }
</style>
</head>
<body>
  <main class="poster">
    <div class="book-stack-photo" role="img" aria-label="Photograph of a tall stack of books tinted magenta"></div>

    <svg class="headline" viewBox="0 0 800 1200" aria-label="Hush Until Stories Happen">
      <text x="690" y="170" text-anchor="end">HUSH</text>
      <text x="690" y="322" text-anchor="end">UNTIL</text>
      <text x="690" y="474" text-anchor="end">STO</text>
      <text x="690" y="626" text-anchor="end">RIES</text>
      <text x="690" y="778" text-anchor="end">HAP</text>
      <text x="690" y="930" text-anchor="end">PEN</text>
    </svg>

    <section class="credit">
      <p class="credit-lead">PRESENTED BY</p>
      <p class="credit-org">PACIFIC COAST<br>SCHOOL MEDIA GUILD</p>
    </section>

    <p class="event-date">MON // OCTOBER 26 // 2020</p>
  </main>
</body>
</html>
```